Design for Training Manuals

We need a graphic design for new training manuals for our organization called Lanternfield Trust, Inc. We are a children's rights NGO based in the Philippines. We are running an advocacy campaign called Raise Every Hand which advocates for the prevention of child sexual abuse and sexual exploitation of children. The Raise Every Hand Campaign is gaining momentum in various countries around the world and we would like to provide our constituents with inspiring training materials that will enable them to carry out the work of protecting children's rights.
Because of the sensitive nature of the subject matter, we would like to present a non-threatening light design, with a creative edge, that incorporates our Raise Every Hand logo. Also, I have attached an image from which you can design from.
Please feel free to visit our website for inspiration: www.lanternfieldtrust.org
Updates
Dear Designers,
I am excited about this project. I have uploaded a couple of our training modules. Overall there are 2 levels: Level 1 with 3 training modules and Level 2 also with 3 training modules.
Thank you,
Teresa
Target Market(s)
Non-government workers, government workers, teachers, social workers...
Industry/Entity Type
Graphic Design
Look and feel
Each slider illustrates characteristics of the customer's brand and the style your logo design should communicate.

```html
<!DOCTYPE html>
<html lang="en">
<head>
<meta charset="utf-8">
<title>Raise Every Hand – Level Three Training Manual</title>
<link rel="stylesheet" href="https://fonts.googleapis.com/css2?family=Playfair+Display:wght@700;900&family=Arimo:wght@400;700&display=swap">
<style>
  :root {
    --page-bg: #ffffff;
    --cover-bg: #fdfdfd;
    --frame: #9a9a9a;
    --teal-deep: #6a9391;
    --sage-light: #abc2b3;
    --ink: #222222;
    --ink-soft: #555555;
    --mark-sun: #e8832a;
    --white: #ffffff;
  }
  * { margin: 0; padding: 0; box-sizing: border-box; }
  html, body {
    width: 1200px; height: 1000px; overflow: hidden;
    background: var(--page-bg);
  }
  .canvas { position: relative; width: 1200px; height: 1000px; }
  .cover-art { position: absolute; left: 0; top: 0; }
  .cover-art .frame { fill: var(--cover-bg); stroke: var(--frame); stroke-width: 2; }
  .cover-art .deep { fill: var(--teal-deep); }
  .cover-art .light { fill: var(--sage-light); }

  .org-mark {
    position: absolute; left: 770px; top: 112px; width: 132px;
    text-align: center;
    font-family: "Arimo", Arial, sans-serif; font-weight: 700;
    font-size: 9px; color: var(--ink); letter-spacing: 0.2px;
  }
  .org-mark .sun {
    display: block; width: 52px; height: 52px; margin: 0 auto 6px;
    border-radius: 50%; background: var(--mark-sun);
  }

  .level {
    position: absolute; left: 521px; top: 248px;
    font-family: "Playfair Display", Georgia, serif; font-weight: 700;
    white-space: nowrap; line-height: 1;
  }
  .level .word { color: var(--teal-deep); font-size: 32px; }
  .level .number { color: var(--sage-light); font-size: 46px; }
  .module-title {
    position: absolute; left: 522px; top: 296px;
    font-family: "Arimo", Arial, sans-serif; font-size: 16px; color: var(--ink);
  }

  .campaign-title {
    position: absolute; font-family: "Playfair Display", Georgia, serif;
    font-weight: 900; color: var(--white); line-height: 1; white-space: nowrap;
  }
  .campaign-title.line-1 { left: 343px; top: 462px; font-size: 90px; }
  .campaign-title.line-2 { left: 430px; top: 545px; font-size: 84px; }
  .campaign-title.line-3 { left: 430px; top: 620px; font-size: 150px; letter-spacing: -2px; }

  .tagline {
    position: absolute; left: 469px; top: 762px;
    font-family: "Arimo", Arial, sans-serif; font-size: 18px; color: var(--ink);
  }

  .publisher {
    position: absolute; left: 300px; top: 857px;
    font-family: "Arimo", Arial, sans-serif; font-size: 13px; color: var(--ink-soft);
    line-height: 18px;
  }
  .publisher .url { display: block; padding-left: 18px; }
</style>
</head>
<body>
<main class="canvas">
  <svg class="cover-art" width="1200" height="1000" viewBox="0 0 1200 1000" aria-hidden="true">
    <rect class="frame" x="281" y="86" width="639" height="827"/>
    <polygon class="deep" points="281,87 485,87 485,755 486,755 281,551"/>
    <polygon class="light" points="485,445 561,372 713,523 488,755 485,755"/>
    <polygon class="deep" points="713,523 713,755 488,755"/>
    <polygon class="light" points="713,523 865,372 715,755 713,755"/>
    <polygon class="deep" points="865,372 919,372 919,630 800,755 715,755"/>
    <polygon class="light" points="919,630 800,755 919,875"/>
  </svg>

  <div class="org-mark"><span class="sun"></span>LANTERNFIELD TRUST INC.</div>

  <div class="level"><span class="word">level</span><span class="number">three</span></div>
  <div class="module-title">Module I: Module Title</div>

  <h1>
    <span class="campaign-title line-1">raise</span>
    <span class="campaign-title line-2">every</span>
    <span class="campaign-title line-3">Hand</span>
  </h1>
  <p class="tagline">Stop child sexual abuse and exploitation</p>

  <p class="publisher">LANTERNFIELD TRUST, INC.<span class="url">www.lanternfieldtrust.org</span></p>
</main>
</body>
</html>
```